Design some Business Cards, Stationary and facebook banner/profile picture for Brookhollow Dental Spa

We are opening a brand new dental practice called "Brookhollow Dental Spa". We offer state of the art dentistry as well as injectables etc for wrinkle reduction and lip enhancement. We have a logo which can be seen at our website brookhollowdentalspa.com.au. We would like the business cards to have room to write appointments on the back (Day/Date/Time)-probably about 3 lines (to make 3 seperate appointments) with a line underneath stating "Please give at least 24hrs notice to change or cancel appointments.". The logo need only appear on the front of the card. We want the feel to be warm and not too clinical. Colours are beige, brown and the blue/green logo. We will also require A5 and A4 letterheads, envelopes, and "with compliments" slips.

Brookhollow Dental Spa
Suite 5, 417-423 Talbeck Rd
East Varnley NSW 2250
Ph (02) 4817-6052
Email - brookhollowdentalspa@[login to view URL]
Website - [login to view URL]

```html
<!DOCTYPE html>
<html lang="en">
<head>
<meta charset="utf-8">
<title>Brookhollow Dental Spa – Stationery Suite</title>
<link href="https://fonts.googleapis.com/css2?family=Mukta:wght@400;600;700&display=swap" rel="stylesheet">
<style>
  :root {
    --bg: #000000;
    --cream-light: #fdf1cc;
    --cream: #f5e6be;
    --cream-deep: #efdcaa;
    --box-tint: rgba(200, 180, 130, 0.22);
    --teal: #2a9fc0;
    --teal-soft: rgba(42, 159, 192, 0.12);
    --ink: #111111;
    --brown: #5b4a3a;
    --paper: #ffffff;
    --paper-grey: #f3f3f4;
    --sky: #bfe4f3;
    --sky-deep: #49aedc;
    --line: #222222;
  }
  * { box-sizing: border-box; margin: 0; padding: 0; }
  html, body { width: 1200px; height: 2400px; overflow: hidden; background: var(--bg); }
  body { position: relative; font-family: "Mukta", Arial, sans-serif; color: var(--ink); }

  .sheet { position: absolute; }

  /* Business card */
  .card { width: 374px; height: 623px; top: 54px; border-radius: 7px; overflow: hidden;
    background: linear-gradient(180deg, var(--cream-light), var(--cream)); }
  .card-front { left: 208px; }
  .card-back { left: 627px; }

  .holder { position: absolute; right: 30px; top: 40px; text-align: right; line-height: 1.15; }
  .holder-name { font-size: 27px; font-weight: 600; }
  .holder-role { font-size: 22px; font-weight: 600; margin-top: 2px; }

  .brand { display: flex; flex-direction: column; align-items: center; color: var(--teal); font-weight: 600; }
  .brand-dot { border-radius: 50%; background: var(--teal); }
  .brand-name { text-align: center; line-height: 1.05; }

  .card-front .brand { position: absolute; left: 0; right: 0; top: 196px; }
  .card-front .brand-dot { width: 90px; height: 90px; margin-bottom: 40px; }
  .card-front .brand-name { font-size: 38px; }

  .contact { position: absolute; left: 0; right: 0; top: 466px; text-align: center;
    font-size: 18px; font-weight: 600; line-height: 24px; }

  .appointment-label { position: absolute; left: 36px; font-size: 17px; font-weight: 600; line-height: 20px; }
  .appointment-box { position: absolute; left: 26px; width: 322px; height: 111px;
    background: var(--box-tint); border-radius: 5px; padding: 8px 14px 0 10px; }
  .field { display: flex; align-items: flex-end; height: 29px; font-size: 17px; font-weight: 600; line-height: 22px; }
  .field-label { width: 44px; }
  .field-line { flex: 1; border-bottom: 3px dashed var(--ink); margin-bottom: 6px; }
  .notice { position: absolute; left: 36px; top: 536px; font-size: 15px; font-weight: 600; line-height: 19px; }

  .watermark { position: absolute; font-weight: 600; text-align: center; line-height: 1.05; }
  .card-back .watermark { left: 0; right: 0; top: 250px; font-size: 46px; color: rgba(120, 150, 150, 0.13); }

  /* Envelopes */
  .envelope-front { left: 277px; top: 718px; width: 743px; height: 342px;
    background: linear-gradient(90deg, var(--cream-deep), var(--cream-light)); }
  .envelope-front .brand { position: absolute; left: 12px; top: 16px; align-items: flex-start; }
  .envelope-front .brand-dot { width: 44px; height: 44px; margin: 0 0 8px 34px; }
  .envelope-front .brand-name { font-size: 22px; text-align: left; }
  .envelope-address { position: absolute; left: 10px; top: 302px; font-size: 12px; font-weight: 600;
    color: var(--brown); line-height: 17px; }
  .envelope-address .url { padding-left: 60px; }

  .envelope-back { left: 271px; top: 1074px; width: 744px; height: 342px; background: var(--paper-grey); overflow: hidden; }
  .envelope-back svg { position: absolute; left: 0; top: 0; }
  .envelope-back .brand { position: absolute; left: 0; right: 0; top: 14px; }
  .envelope-back .brand-dot { width: 22px; height: 22px; margin-bottom: 3px; }
  .envelope-back .brand-name { font-size: 11px; }

  /* Letterhead */
  .letterhead { left: 51px; top: 1440px; width: 637px; height: 940px; background: var(--paper); }
  .sky-band { position: absolute; left: 0; top: 0; width: 100%;
    background: linear-gradient(170deg, var(--sky) 0%, #eaf7fc 35%, var(--sky-deep) 70%, var(--sky) 100%); }
  .letterhead .sky-band { height: 94px; }
  .letterhead .brand { position: absolute; right: 6px; top: 8px; align-items: flex-end; }
  .letterhead .brand-dot { width: 34px; height: 34px; margin: 0 22px 4px 0; }
  .letterhead .brand-name { font-size: 15px; text-align: right; }
  .letterhead-url { position: absolute; right: 4px; top: 76px; font-size: 13px; font-weight: 600; color: #1a6f9a; line-height: 16px; }
  .letterhead-footer { position: absolute; left: 0; right: 0; top: 903px; border-top: 2px solid var(--line); }
  .ref-tag { position: absolute; left: 274px; top: -10px; width: 92px; height: 18px; background: var(--paper);
    border: 1.5px solid var(--line); border-radius: 6px; font-size: 10px; text-align: center; line-height: 15px; }
  .footer-text { position: absolute; left: 6px; top: 12px; font-size: 12px; line-height: 16px; color: #333; white-space: nowrap; }

  /* Compliments slip */
  .slip { left: 780px; top: 1590px; width: 375px; height: 454px; background: var(--paper); overflow: hidden; }
  .slip .sky-band { height: 62px; }
  .slip .brand { position: absolute; right: 4px; top: 4px; align-items: flex-end; }
  .slip .brand-dot { width: 28px; height: 28px; margin: 0 20px 3px 0; }
  .slip .brand-name { font-size: 12px; text-align: right; }
  .slip .watermark { left: 0; right: 0; top: 270px; font-size: 46px; color: rgba(140, 170, 190, 0.16); }
  .write-line { position: absolute; left: 12px; width: 348px; border-bottom: 3px dashed var(--ink); }
</style>
</head>
<body>

  <section class="sheet card card-front">
    <div class="holder">
      <div class="holder-name">Elena Marsh</div>
      <div class="holder-role">Dentist</div>
    </div>
    <div class="brand">
      <span class="brand-dot"></span>
      <span class="brand-name">Brookhollow<br>Dental Spa</span>
    </div>
    <div class="contact">
      Suite 5, 417-423 Talbeck Rd<br>
      East Varnley NSW 2250<br>
      Ph (02) 4817-6052<br>
      Email - brookhollowdentalspa@gmail.com<br>
      Website - brookhollowdentalspa.com.au
    </div>
  </section>

  <section class="sheet card card-back">
    <div class="watermark">Brookhollow<br>Dental Spa</div>

    <div class="appointment-label" style="top:18px">Day 1</div>
    <div class="appointment-box" style="top:43px">
      <div class="field"><span class="field-label">Day</span><span class="field-line"></span></div>
      <div class="field"><span class="field-label">Date</span><span class="field-line"></span></div>
      <div class="field"><span class="field-label">Time</span><span class="field-line"></span></div>
    </div>

    <div class="appointment-label" style="top:198px">Day 2</div>
    <div class="appointment-box" style="top:226px">
      <div class="field"><span class="field-label">Day</span><span class="field-line"></span></div>
      <div class="field"><span class="field-label">Date</span><span class="field-line"></span></div>
      <div class="field"><span class="field-label">Time</span><span class="field-line"></span></div>
    </div>

    <div class="appointment-label" style="top:374px">Day3</div>
    <div class="appointment-box" style="top:400px">
      <div class="field"><span class="field-label">Day</span><span class="field-line"></span></div>
      <div class="field"><span class="field-label">Date</span><span class="field-line"></span></div>
      <div class="field"><span class="field-label">Time</span><span class="field-line"></span></div>
    </div>

    <div class="notice">Note: Please give at least 24hrs notice<br>to change or cancel appointments.</div>
  </section>

  <section class="sheet envelope-front">
    <div class="brand">
      <span class="brand-dot"></span>
      <span class="brand-name">Brookhollow<br>Dental Spa</span>
    </div>
    <div class="envelope-address">
      Suite 5, 417-423 Talbeck Rd East Varnley NSW 2250<br>
      <span class="url">brookhollowdentalspa.com.au</span>
    </div>
  </section>

  <section class="sheet envelope-back">
    <svg width="744" height="110" viewBox="0 0 744 110">
      <defs>
        <linearGradient id="flap-fill" x1="0" x2="1" y1="0" y2="0">
          <stop offset="0" stop-color="#f3e3b6"/>
          <stop offset="1" stop-color="#fdf1cc"/>
        </linearGradient>
      </defs>
      <path d="M0 0 H744 V36 Q372 110 0 36 Z" fill="url(#flap-fill)"/>
    </svg>
    <div class="brand">
      <span class="brand-dot"></span>
      <span class="brand-name">Brookhollow Dental Spa</span>
    </div>
  </section>

  <section class="sheet letterhead">
    <div class="sky-band" role="img" aria-label="Soft flowing blue wave header"></div>
    <div class="brand">
      <span class="brand-dot"></span>
      <span class="brand-name">Brookhollow<br>Dental Spa</span>
    </div>
    <div class="letterhead-url">brookhollowdentalspa.com.au</div>
    <div class="letterhead-footer">
      <div class="ref-tag">Req#0000000</div>
      <div class="footer-text">Suite 5, 417-423 Talbeck Rd. East Varnley NSW 2250. Phone (02) 4817-6052. Email - brookhollowdentalspa@gmail.com.</div>
    </div>
  </section>

  <section class="sheet slip">
    <div class="sky-band" role="img" aria-label="Soft flowing blue wave header"></div>
    <div class="brand">
      <span class="brand-dot"></span>
      <span class="brand-name">Brookhollow<br>Dental Spa</span>
    </div>
    <div class="watermark">Brookhollow<br>Dental Spa</div>
    <div class="write-line" style="top:92px"></div>
    <div class="write-line" style="top:146px"></div>
    <div class="write-line" style="top:200px"></div>
    <div class="write-line" style="top:254px"></div>
    <div class="write-line" style="top:308px"></div>
    <div class="write-line" style="top:362px"></div>
    <div class="write-line" style="top:416px"></div>
  </section>

</body>
</html>
```